Recycling Depot Business Card Design

We need a double sided business card for our recycling depot business. Please include name, position, address, phone, cell, fax, email and website address. Business card should match the colour scheme of our logo and look environmental but modern. I've attached a few business cards from Plume Kettle that I like.

Industry/Entity Type

Recycling

Contact Information for Business Card

Please include name, position, address, phone, cell, fax, email and website address.

Font styles to use
Sans Serif

Requirements
Must have
• Our Logo, Colour Scheme that matches our logo. Use of Colour Gradients and a custom look.

```html
<!DOCTYPE html>
<html lang="en">
<head>
<meta charset="utf-8">
<title>Cyclora – Business Card</title>
<link rel="stylesheet" href="https://fonts.googleapis.com/css2?family=Montserrat:wght@500;700;800&family=Lato:wght@400;700&display=swap">
<style>
  :root {
    --stage: #1f1f1f;
    --forest: #1c6637;
    --leaf: #7dbd3b;
    --lime: #9dcb3c;
    --paper: #ffffff;
    --card-w: 540px;
    --card-h: 309px;
  }
  * { box-sizing: border-box; margin: 0; padding: 0; }
  html, body {
    width: 1200px; height: 780px; overflow: hidden;
    background: var(--stage);
  }
  .canvas {
    width: 1200px; height: 780px;
    display: flex; align-items: center; justify-content: center; gap: 40px;
  }
  .card {
    position: relative;
    width: var(--card-w); height: var(--card-h);
    background: var(--paper);
    overflow: hidden;
    box-shadow: 0 12px 30px rgba(0,0,0,.45);
  }
  .card__art { position: absolute; inset: 0; width: 100%; height: 100%; }

  .brand { position: absolute; display: flex; flex-direction: column; }
  .brand__row { display: flex; align-items: center; gap: 10px; }
  .brand__dot { border-radius: 50%; background: var(--leaf); flex: none; }
  .brand__name {
    font-family: "Montserrat", sans-serif; font-weight: 800;
    color: var(--forest); line-height: 1;
  }
  .brand__tagline {
    font-family: "Montserrat", sans-serif; font-weight: 500;
    color: #222; letter-spacing: .06em;
  }

  .card--front .brand { left: 50%; top: 50%; transform: translate(-50%, -58%); }
  .card--front .brand__dot { width: 34px; height: 34px; }
  .card--front .brand__name { font-size: 50px; }
  .card--front .brand__tagline { font-size: 15px; margin-left: 46px; margin-top: 4px; }

  .card--back .brand { left: 26px; top: 92px; }
  .card--back .brand__dot { width: 22px; height: 22px; }
  .card--back .brand__name { font-size: 32px; }
  .card--back .brand__tagline { font-size: 10px; margin-left: 32px; margin-top: 3px; }

  .contact {
    position: absolute; left: 335px; top: 34px;
    color: var(--paper);
  }
  .contact__name {
    font-family: "Montserrat", sans-serif; font-weight: 800;
    font-size: 20px; letter-spacing: -.01em; line-height: 1;
  }
  .contact__name-accent { color: var(--lime); }
  .contact__role {
    font-family: "Lato", sans-serif; font-size: 11px; margin-top: 3px;
  }
  .contact__list { list-style: none; margin-top: 12px; }
  .contact__item {
    display: flex; align-items: flex-start; gap: 9px;
    font-family: "Lato", sans-serif; font-size: 11px; line-height: 1.3;
    margin-bottom: 5px;
  }
  .contact__icon { width: 11px; height: 11px; flex: none; margin-top: 2px; fill: var(--lime); }
</style>
</head>
<body>
<main class="canvas">

  <section class="card card--front" aria-label="Card front">
    <svg class="card__art" viewBox="0 0 540 309" preserveAspectRatio="none" aria-hidden="true">
      <path d="M180,0 L540,0 L540,66 Q330,6 180,0 Z" fill="var(--forest)"/>
      <path d="M540,74 Q320,14 165,0 L150,0 Q320,24 540,82 Z" fill="var(--leaf)"/>
      <path d="M0,244 Q220,300 355,309 L0,309 Z" fill="var(--forest)"/>
      <path d="M0,228 Q230,292 390,309 L372,309 Q220,300 0,237 Z" fill="var(--leaf)"/>
    </svg>
    <div class="brand">
      <div class="brand__row">
        <span class="brand__dot"></span>
        <span class="brand__name">Cyclora</span>
      </div>
      <span class="brand__tagline">Resource Recovery</span>
    </div>
  </section>

  <section class="card card--back" aria-label="Card back">
    <svg class="card__art" viewBox="0 0 540 309" preserveAspectRatio="none" aria-hidden="true">
      <defs>
        <linearGradient id="band" x1="0" y1="1" x2="1" y2="0">
          <stop offset="0" stop-color="var(--lime)"/>
          <stop offset="1" stop-color="#5fae44"/>
        </linearGradient>
      </defs>
      <rect width="540" height="309" fill="url(#band)"/>
      <path d="M0,0 L540,0 L540,196 C380,232 150,222 0,172 Z" fill="var(--forest)"/>
      <path d="M0,174 C150,224 380,234 540,198" fill="none" stroke="var(--paper)" stroke-width="4"/>
      <path d="M0,0 L350,0 C304,50 314,125 264,153 C206,180 100,172 0,164 Z" fill="var(--paper)"/>
      <path d="M0,0 L344,0 C298,50 308,122 258,150 C200,176 100,168 0,160 Z" fill="var(--leaf)"/>
      <path d="M0,0 L305,0 C282,50 292,115 245,142 C195,165 100,161 0,156 Z" fill="var(--paper)"/>
    </svg>

    <div class="brand">
      <div class="brand__row">
        <span class="brand__dot"></span>
        <span class="brand__name">Cyclora</span>
      </div>
      <span class="brand__tagline">Resource Recovery</span>
    </div>

    <div class="contact">
      <h1 class="contact__name">YOUR <span class="contact__name-accent">NAMEHERE</span></h1>
      <p class="contact__role">Designation</p>
      <ul class="contact__list">
        <li class="contact__item">
          <svg class="contact__icon" viewBox="0 0 12 12"><path d="M6 0a4 4 0 0 0-4 4c0 3 4 8 4 8s4-5 4-8a4 4 0 0 0-4-4zm0 5.5A1.5 1.5 0 1 1 6 2.5a1.5 1.5 0 0 1 0 3z"/></svg>
          <span>123 Your address, Goes here,<br>Dummy Text, Now 456</span>
        </li>
        <li class="contact__item">
          <svg class="contact__icon" viewBox="0 0 12 12"><path d="M0 2h12v8H0z M0 2l6 4.5L12 2" stroke="var(--forest)" stroke-width=".8"/></svg>
          <span>hello@cyclora-depot.com</span>
        </li>
        <li class="contact__item">
          <svg class="contact__icon" viewBox="0 0 12 12"><circle cx="6" cy="6" r="5.5"/><path d="M0.5 6h11M6 .5v11M2 3h8M2 9h8" stroke="var(--forest)" stroke-width=".7" fill="none"/></svg>
          <span>www.cyclora-depot.com</span>
        </li>
        <li class="contact__item">
          <svg class="contact__icon" viewBox="0 0 12 12"><path d="M2.5 0.5l2 2.5-1.2 1.5a7 7 0 0 0 4.2 4.2L9 7.5l2.5 2-1.5 2C5 11 1 7 .5 2z"/></svg>
          <span>+01 234 567 8900</span>
        </li>
        <li class="contact__item">
          <svg class="contact__icon" viewBox="0 0 12 12"><path d="M3 0h5v4H3z M0 5h12v7H0z"/></svg>
          <span>+01 234 567 8900</span>
        </li>
      </ul>
    </div>
  </section>

</main>
</body>
</html>
```